Looking for someone to design a business card for my plumbing business Brindle Plumbing Solutions I want the background also to be black, must attract clients. If possible I want the front to be the logo and the back to show maybe the details.

Target Market(s)

Clients

Industry/Entity Type

Plumbing maintenance

Contact Information for Business Card

Name: Dylan, Contact: 0451 306 729, Email: brindleplumbingsolutions@mailpost.example, Licence number 728094K

Font styles to use
Other font styles liked:
• as per logo maybe?

Colors

Designer to choose colors to be used in the design.

Requirements
Nice to have
• stating the service I provide, emergency plumbing, plumbing maintenance, drainage maintenance, block sewer and stormwater, camera and locating.

```html
<!DOCTYPE html>
<html lang="en">
<head>
<meta charset="utf-8">
<title>Brindle Plumbing Solutions – Business Card</title>
<link rel="stylesheet" href="https://fonts.googleapis.com/css2?family=Montserrat:wght@500;700&display=swap">
<style>
  :root {
    --stage: #3b3b3b;
    --card: #141414;
    --card-edge: #1c1c1c;
    --ink: #f4f4f4;
    --silver: #d6d6d6;
    --accent: #4a90d6;
  }
  * { margin: 0; padding: 0; box-sizing: border-box; }
  html, body {
    width: 1200px; height: 689px; overflow: hidden;
    background: var(--stage);
    font-family: "Montserrat", sans-serif;
  }
  .stage {
    position: relative; width: 1200px; height: 689px;
    display: flex; align-items: center; justify-content: center; gap: 40px;
  }
  .card {
    position: relative; width: 540px; height: 309px;
    border-radius: 18px;
    background: var(--card);
    box-shadow: 0 18px 40px rgba(0,0,0,.45);
    overflow: hidden;
  }
  .card--front {
    background: linear-gradient(120deg, #1e1e1e 0%, #121212 45%, #0d0d0d 100%);
  }
  .front-wordmark {
    position: absolute; inset: 0;
    display: flex; flex-direction: column; align-items: center; justify-content: center;
    color: var(--silver); font-weight: 700; text-transform: uppercase; text-align: center;
  }
  .front-wordmark .brand-main { font-size: 46px; letter-spacing: 2px; line-height: 1; }
  .front-wordmark .brand-sub { font-size: 17px; letter-spacing: 3px; margin-top: 8px; }

  .back-wordmark {
    position: absolute; right: 34px; top: 52px;
    color: var(--ink); font-weight: 700; text-transform: uppercase; text-align: right;
  }
  .back-wordmark .brand-main { font-size: 36px; letter-spacing: 1.5px; line-height: 1; }
  .back-wordmark .brand-sub { font-size: 13px; letter-spacing: 2.5px; margin-top: 6px; }

  .licence {
    position: absolute; right: 34px; top: 148px;
    color: var(--ink); font-size: 12px; font-weight: 500; letter-spacing: .3px;
  }
  .contact {
    position: absolute; left: 34px; bottom: 34px;
    color: var(--ink);
  }
  .contact .person {
    color: var(--accent); font-weight: 700; font-size: 26px; margin-bottom: 14px;
  }
  .contact .line {
    display: flex; align-items: center; gap: 9px;
    font-size: 12.5px; font-weight: 500; margin-top: 6px;
  }
  .contact svg { width: 13px; height: 13px; flex: none; fill: var(--accent); }
</style>
</head>
<body>
<main class="stage">
  <section class="card card--front" aria-label="Card front">
    <div class="front-wordmark">
      <span class="brand-main">Brindle</span>
      <span class="brand-sub">Plumbing Solutions</span>
    </div>
  </section>

  <section class="card card--back" aria-label="Card back">
    <div class="back-wordmark">
      <div class="brand-main">Brindle</div>
      <div class="brand-sub">Plumbing Solutions</div>
    </div>
    <p class="licence">Licence number 728094K</p>
    <div class="contact">
      <p class="person">Dylan</p>
      <p class="line">
        <svg viewBox="0 0 24 24" aria-hidden="true"><path d="M6.6 10.8a15.1 15.1 0 0 0 6.6 6.6l2.2-2.2a1 1 0 0 1 1-.25 11.4 11.4 0 0 0 3.6.57 1 1 0 0 1 1 1V20a1 1 0 0 1-1 1A17 17 0 0 1 3 4a1 1 0 0 1 1-1h3.5a1 1 0 0 1 1 1c0 1.25.2 2.45.57 3.57a1 1 0 0 1-.25 1z"/></svg>
        0451 306 729
      </p>
      <p class="line">
        <svg viewBox="0 0 24 24" aria-hidden="true"><path d="M2 5h20v14H2zm2 2v.5l8 5 8-5V7zm0 2.9V17h16V9.9l-8 5z"/></svg>
        brindleplumbingsolutions@mailpost.example
      </p>
    </div>
  </section>
</main>
</body>
</html>
```